4 x Florist Footpath Signage Boards that are consistant with each other for a modern florist

Eye catching, easy to read. little bit floral.
See example attached for wording. We are a modern florist in a country town.
This will be out on the street and needs to stand out!!

The Signage Panels
1. Valentines Day - 14th Feb
2. Workshop Signage boards - see attached example
3. Mothers Day Signage Board - 'Treat mum this Mothers Day'
4. We Are Open

Attached is a copy of the design guidelines and the template. the base of the sign is white.

Target Market(s)

Modern

Industry/Entity Type

Florist

Font styles to use
Sans Serif

Colors
eea4c8
f59296
ffffff
757575

Requirements
Must have
• flowers
• weddings
• giftware
• workshops
• flowers make people happy
• odettemarshpetals.co.nz
Nice to have
• Logo
• little bit of floral or greenery
• my shop is modem and industrial
Should not have
• Needs to be able to read easy

```html
<!DOCTYPE html>
<html lang="en">
<head>
<meta charset="utf-8">
<title>Odette Marsh Petals – Footpath Sign</title>
<link rel="stylesheet" href="https://fonts.googleapis.com/css2?family=Roboto+Condensed:wght@700&family=Open+Sans:wght@800&family=Oswald:wght@300&family=Playfair+Display:wght@700&display=swap">
<style>
  :root {
    --blush: #fcecea;
    --blossom: #f5b3b3;
    --blossom-deep: #e39a9e;
    --grey: #757575;
    --plum: #9e3d70;
    --ink: #000000;
    --gold: #c9a75e;
    --happy-fill: #e6dedc;
  }
  html, body {
    margin: 0;
    padding: 0;
    overflow: hidden;
  }
  .sign {
    position: relative;
    width: 905px;
    height: 1200px;
    background: var(--blush);
    overflow: hidden;
  }
  .blossom-top {
    position: absolute;
    left: 0;
    top: 0;
    width: 905px;
    height: 370px;
    background:
      radial-gradient(ellipse 200px 170px at 90px 260px, rgba(245,150,150,.55), transparent 70%),
      radial-gradient(ellipse 360px 120px at 420px 120px, rgba(227,154,158,.45), transparent 72%),
      radial-gradient(ellipse 260px 90px at 680px 120px, rgba(227,154,158,.35), transparent 72%),
      linear-gradient(180deg, rgba(245,179,179,.35), transparent);
  }
  .blossom-bottom {
    position: absolute;
    left: 420px;
    top: 850px;
    width: 485px;
    height: 350px;
    background:
      radial-gradient(ellipse 220px 150px at 330px 230px, rgba(245,150,150,.5), transparent 70%),
      radial-gradient(ellipse 200px 110px at 160px 260px, rgba(227,154,158,.4), transparent 72%),
      linear-gradient(0deg, rgba(245,179,179,.3), transparent);
  }
  .blossom-corner {
    position: absolute;
    left: 120px;
    top: 1080px;
    width: 260px;
    height: 120px;
    background: radial-gradient(ellipse 130px 70px at 100px 90px, rgba(245,150,150,.35), transparent 72%);
  }
  .type {
    position: absolute;
    inset: 0;
  }
  .headline { font-family: "Roboto Condensed", "Arial Narrow", sans-serif; font-weight: 700; fill: var(--grey); }
  .headline-happy {
    font-family: "Playfair Display", Georgia, serif;
    font-weight: 700;
    fill: var(--happy-fill);
    stroke: var(--grey);
    stroke-width: 5;
    stroke-linejoin: round;
    paint-order: stroke fill;
  }
  .services { font-family: "Open Sans", Arial, sans-serif; font-weight: 800; fill: var(--plum); }
  .cta { font-family: "Open Sans", Arial, sans-serif; font-weight: 800; fill: var(--ink); }
  .web-address { font-family: "Oswald", "Arial Narrow", sans-serif; font-weight: 300; fill: var(--ink); }
  .brand-name { font-family: "Oswald", "Arial Narrow", sans-serif; font-weight: 300; fill: var(--gold); }
</style>
</head>
<body>
<main class="sign">
  <div class="blossom-top" role="img" aria-label="Cherry blossom branches with pink flowers across the top"></div>
  <div class="blossom-bottom" role="img" aria-label="Cherry blossom branch with pink flowers at the lower right"></div>
  <div class="blossom-corner" role="img" aria-label="Faint pink blossom at the bottom"></div>

  <svg class="type" width="905" height="1200" viewBox="0 0 905 1200">
    <g class="brand">
      <text class="brand-name" x="788" y="212" font-size="17" letter-spacing="4" text-anchor="middle">ODETTE MARSH</text>
      <text class="brand-name" x="788" y="236" font-size="13" letter-spacing="4" text-anchor="middle">PETALS</text>
    </g>

    <text class="headline" x="151" y="459" font-size="128" textLength="465" lengthAdjust="spacingAndGlyphs">FLOWERS</text>
    <text class="headline" x="643" y="459" font-size="90" textLength="196" lengthAdjust="spacingAndGlyphs">MAKE</text>
    <text class="headline" x="64" y="599" font-size="101" textLength="247" lengthAdjust="spacingAndGlyphs">PEOPLE</text>
    <text class="headline-happy" x="338" y="602" font-size="150" textLength="512" lengthAdjust="spacingAndGlyphs">HAPPY</text>

    <g class="service-list">
      <text class="services" x="448" y="691" font-size="40" text-anchor="middle" textLength="248" lengthAdjust="spacing">FLOWERS</text>
      <text class="services" x="448" y="757" font-size="40" text-anchor="middle" textLength="290" lengthAdjust="spacing">WEDDINGS</text>
      <text class="services" x="448" y="824" font-size="40" text-anchor="middle" textLength="280" lengthAdjust="spacing">GIFTWARE</text>
      <text class="services" x="448" y="890" font-size="40" text-anchor="middle" textLength="338" lengthAdjust="spacing">WORKSHOPS</text>
    </g>

    <text class="cta" x="64" y="1003" font-size="48" textLength="358" lengthAdjust="spacing">SHOP ONLINE</text>
    <text class="web-address" x="64" y="1064" font-size="52" textLength="628" lengthAdjust="spacing">odettemarshpetals.co.nz</text>
  </svg>
</main>
</body>
</html>
```